'The Paperlanterns' - Album Artwork Needed!!

Looking for album artwork design for a new pop/rock original band from NJ called 'The Paperlanterns'. The debut EP is entitled 'Hold the Door'.

The group is a 4 piece with a lead singer/guitar player, bass player, guitar player, and drummer. There are also piano parts on the songs played by the singer. Stylistically similar to a Bright Harbor Kids/Folds the Map/Vesper kind of vibe.

We need designs for both the front and rear of the CD sleeve as well as printing on the CD itself. We're leaning towards photo based artwork that captures the intensity of our music but we are not opposed to graphic design.

If there were a mission statement and an idea we would want to convey for the band it would be fun, energetic, happy, feel good, pumped up, moving, dynamic, get people going, powerful, lively rock songs with catchy hooks.

Energy! Energy! Energy!

Give me your best work! Lets get vibrant fun and memorable.

Let me know if you have questions!

Reason: Definitely some good designs. Going to extend it for 5 days in case there are any extras. Still open....

Reason: Still trying to narrow down the right paperlanterns EP cover. Some great designs so far. We need to pick one within the next 7 days so nows the last chance. Think colorful and fun! Let me know if you h ave any questions

Hi Designers, Seen some great work! We need to send the CD off to get manufactured so we need to pick our design ASAP! We've changed this to a committed payment project. We also increased the payment amount and listed this as a featured project. Bring your best work and please view the brief first. Any questions be sure to ask!

Reason: We've increased the payment and upgraded this to a committed project. We want to see what you've got! This is our absolute deadline as the CD needs to get manufactured ASAP! Thanks!

A lot of good ideas, not sure we found the one that captures the vibe we're going for, but we definitely need to pick ASAP! Message us if you have questions! Theo

Reason: More Designs!

Designer's - great work is coming in. Please use the font: JennaSue.ttf for the band's name 'The Paperlanterns'. The rest is all open to interpretation. Remember colorful fun and energetic!

...Also we've decided to remove the last two bonus tracks so the EP is only going to be the 5 songs: 1.) The Undertow 2.) Edge of the Porch 3.) Marnie 4.) Drifters 5.) Running Late Always Felt So Right

Designers! I have uploaded a file that contains the template for the artwork. The design will need to fit these template. Theres one for the outside of the CD and another for the face of the CD. Please let me know if you have any questions! Thank you, Theo

Target Market(s)

Younger audience 16-30

Industry/Entity Type

Printing

Requirements
Must have
• Vibrant in either color or photography
Should not have
• Photos of the band members as the design.

I provided from photos so you can get an idea for the band, but I do NOT want those used as the album artwork.

Please do not use these pictures on your design!
Thanks!

```html
<!DOCTYPE html>
<html lang="en">
<head>
<meta charset="utf-8">
<title>The Paperlanterns – Hold the Door – CD Sleeve</title>
<link rel="stylesheet" href="https://fonts.googleapis.com/css2?family=Cinzel:wght@400;600&family=Oswald:wght@700&display=swap">
<style>
  :root {
    --canvas: #ffffff;
    --ink-white: #ffffff;
    --ink-black: #0b0b0b;
    --front-dark: #0a0a08;
    --front-ember: #b8401a;
    --front-rust: #6e2a10;
    --front-moss: #5f9a3c;
    --front-mist: #cfe3b8;
    --front-water: #3f7f6c;
    --back-gold: #d9cc3a;
    --back-olive: #8f8a22;
    --back-forest: #243d1f;
    --back-umber: #4a2c14;
    --back-light: #f1e98a;
  }
  * { margin: 0; padding: 0; box-sizing: border-box; }
  html, body {
    width: 1200px;
    height: 628px;
    overflow: hidden;
    background: var(--canvas);
  }
  .sleeve {
    position: relative;
    width: 1200px;
    height: 628px;
  }
  .panel {
    position: absolute;
    top: 44px;
    width: 547px;
    height: 547px;
    overflow: hidden;
  }
  .panel--front { left: 34px; }
  .panel--back { left: 620px; }

  .artwork {
    position: absolute;
    inset: 0;
  }
  .artwork--front {
    background:
      radial-gradient(circle at 173px 105px, rgba(255,255,255,0.95) 0 4px, rgba(255,255,255,0.25) 10px, transparent 28px),
      radial-gradient(ellipse 230px 160px at 330px 460px, var(--front-water) 0%, transparent 75%),
      radial-gradient(ellipse 200px 170px at 420px 220px, var(--front-mist) 0%, transparent 70%),
      radial-gradient(ellipse 260px 220px at 360px 300px, var(--front-moss) 0%, transparent 75%),
      radial-gradient(ellipse 170px 260px at 60px 290px, var(--front-ember) 0%, var(--front-rust) 45%, transparent 80%),
      linear-gradient(160deg, var(--front-dark) 0%, #1d2a14 45%, #203a2c 75%, var(--front-dark) 100%);
  }
  .artwork--back {
    background:
      radial-gradient(ellipse 150px 110px at 220px 40px, var(--back-light) 0%, transparent 75%),
      linear-gradient(200deg, transparent 48%, rgba(74,44,20,0.75) 58%, transparent 70%),
      radial-gradient(ellipse 300px 90px at 180px 330px, var(--back-forest) 0%, transparent 80%),
      radial-gradient(ellipse 220px 200px at 90px 160px, var(--back-gold) 0%, transparent 80%),
      radial-gradient(ellipse 200px 260px at 460px 300px, var(--back-umber) 0%, transparent 80%),
      linear-gradient(170deg, var(--back-gold) 0%, var(--back-olive) 55%, #5d5a1a 100%);
  }

  .title-block {
    position: absolute;
    right: 139px;
    top: 104px;
    text-align: right;
  }
  .band-article,
  .band-name {
    font-family: "Cinzel", "Times New Roman", serif;
    font-weight: 400;
    color: var(--ink-white);
    line-height: 1;
  }
  .band-article {
    font-size: 34px;
    text-align: center;
    padding-left: 40px;
    letter-spacing: 1px;
  }
  .band-name {
    font-size: 26px;
    margin-top: 4px;
    letter-spacing: 0;
  }
  .album-title {
    font-family: "Oswald", "Arial Narrow", sans-serif;
    font-weight: 700;
    font-size: 56px;
    line-height: 1;
    color: var(--ink-black);
    margin-top: 6px;
    letter-spacing: -0.5px;
  }

  .track-column {
    position: absolute;
    left: 0;
    right: 0;
    top: 140px;
    text-align: center;
    list-style: none;
  }
  .track-column li {
    font-family: Arial, Helvetica, sans-serif;
    font-size: 10px;
    line-height: 30.5px;
    color: var(--ink-white);
    text-transform: uppercase;
  }
  .liner-note {
    position: absolute;
    left: 14px;
    right: 12px;
    top: 455px;
    font-family: Arial, Helvetica, sans-serif;
    font-size: 9.4px;
    line-height: 13px;
    color: var(--ink-white);
    text-align: center;
    text-transform: uppercase;
  }
</style>
</head>
<body>
  <main class="sleeve">
    <section class="panel panel--front" aria-label="Front cover">
      <div class="artwork artwork--front" role="img" aria-label="Cover illustration: dark rocky shoreline with a bright star, a fiery orange cliff on the left, a green crashing wave and rippling teal water"></div>
      <div class="title-block">
        <p class="band-article">THE</p>
        <h1 class="band-name">PAPERLANTERNS</h1>
        <h2 class="album-title">HOLD THE DOOR</h2>
      </div>
    </section>

    <section class="panel panel--back" aria-label="Back cover">
      <div class="artwork artwork--back" role="img" aria-label="Back illustration: glowing yellow sky with lightning streaks over a dark green hillside and brown diagonal rock"></div>
      <ul class="track-column">
        <li>Lorem ipsum dolor sit amet,</li>
        <li>consectetur adipisicing elit,</li>
        <li>sed do eiusmod t</li>
        <li>empor incididunt</li>
        <li>ut labore et dolo</li>
        <li>re magna aliqua.</li>
        <li>Ut enim ad minim</li>
        <li>veniam,</li>
        <li>quis nostrud exercitation</li>
      </ul>
      <p class="liner-note">Lorem ipsum dolor sit amet, consectetur adipisicing elit, sed do eiusmod tempor incididunt ut labore et dolore magna aliqua. Ut enim ad minim veniam, quis nostrud exercitation ullamco laboris nisi ut aliquip ex ea commodo consequat. Duis aute irure dolor in reprehenderit in voluptate velit esse cillum dolore eu fugiat nulla pariatur. Excepteur sint occaecat cupidatat non proident, sunt in culpa qui officia deserunt mollit anim id est laborum."</p>
    </section>
  </main>
</body>
</html>
```